Broschüre für Anbieter von Haushaltshilfen und Alltagsbegleitern für Privathaushalte
Zielgruppe
Wir bieten Haushaltshilfen und Alltagsbegleiter für Privathaushalte an. Unsere Hauptkundenklientel sind Pflegebedürftige Menschen denen eine Haushaltshilfe von der Pflegekasse zusteht. Weitere Kunden sind Familien und/oder Singlehaushalte, die eine Haushaltfshilfe benötigen.
Aufgabenstellung
- Das Prospekt sollte DIN A4 sein, sind aber auch offen für andere Formate
- Farbdesign muß unsere Logofarben enthalten
- In dem Prospekt müßen unsere Leistungen wie auf unserer Internetseite www.lindaufeld.de beschrieben sein.
- Seitenanzahl insgesamt 4 Seiten

```html
<!DOCTYPE html>
<html lang="de">
<head>
<meta charset="utf-8">
<title>Broschüre Haushaltshilfe – Innenseiten</title>
<link href="https://fonts.googleapis.com/css2?family=Roboto+Condensed:wght@700&family=Roboto:wght@400&display=swap" rel="stylesheet">
<style>
  :root{
    --red:#c0141e;
    --red-dark:#9c1219;
    --red-mid:#b01620;
    --text:#3a3a3a;
    --paper:#ffffff;
    --line:#9a9a9a;
  }
  html,body{margin:0;padding:0;overflow:hidden;background:#fff}
  .spread{position:relative;width:1200px;height:849px;background:var(--paper);overflow:hidden;font-family:"Roboto",Arial,sans-serif;color:var(--text);box-sizing:border-box;border:1px solid var(--line)}
  .page{position:absolute;top:0;height:100%}
  .page--left{left:0;width:601px;border-right:1px solid var(--line)}
  .page--right{left:601px;width:599px}
  .hero{position:absolute;left:0;top:0}
  h2{font-family:"Roboto Condensed","Arial Narrow",sans-serif;font-weight:700;color:var(--red);font-size:26px;margin:0;line-height:1;position:absolute}
  .body-text{position:absolute;font-size:12.4px;line-height:18.5px;margin:0}
  .about h2{left:43px;top:432px}
  .about .body-text{left:43px;top:465px;width:490px}
  .benefits h2{left:43px;top:585px}
  .benefit{position:absolute;top:636px;width:140px}
  .benefit svg{display:block;height:60px}
  .benefit p{margin:14px 0 0;font-size:12.8px;line-height:18.5px}
  .offers h2{left:72px;top:72px;font-size:25px}
  .offers .body-text{left:72px;top:104px;width:470px;font-size:12.4px}
  .service{position:absolute;width:150px}
  .service .tile{width:125px;height:98px;border:3px solid var(--red);border-radius:6px;display:flex;align-items:center;justify-content:center}
  .service .tile svg{width:72px;height:72px;fill:none;stroke:var(--red);stroke-width:2.4;stroke-linecap:round;stroke-linejoin:round}
  .service span{display:block;margin-top:8px;font-size:19.5px;color:var(--red);white-space:nowrap}
</style>
</head>
<body>
<div class="spread">
  <section class="page page--left">
    <svg class="hero" width="601" height="420" viewBox="0 0 601 420">
      <defs>
        <linearGradient id="photoTone" x1="0" y1="0" x2="1" y2="1">
          <stop offset="0" stop-color="#eeebe7"/>
          <stop offset="0.45" stop-color="#d6c6b2"/>
          <stop offset="1" stop-color="#8f837c"/>
        </linearGradient>
        <clipPath id="heroCut"><polygon points="0,0 601,0 601,348 458,392 73,373 0,417"/></clipPath>
      </defs>
      <rect role="img" aria-label="Foto: junge Frau und Seniorin im Gespräch auf einem Sofa" width="601" height="420" fill="url(#photoTone)" clip-path="url(#heroCut)"/>
      <polygon points="0,330 186,304 458,392 73,373 0,417" fill="var(--red-mid)"/>
      <polygon points="186,304 458,392 73,373 0,417 0,380" fill="var(--red-dark)" opacity="0.55"/>
      <polygon points="601,242 601,348 458,392 408,376" fill="var(--red)"/>
      <polygon points="601,242 458,392 408,376" fill="var(--red-dark)" opacity="0.5"/>
    </svg>

    <div class="about">
      <h2>Über uns</h2>
      <p class="body-text">Wir bieten Haushaltshilfen und Alltagsbegleiter für Privathaushalte an. Unsere Hauptkundenklientel sind Pflegebedürftige Menschen denen eine Haushaltshilfe von der Pflegekasse zusteht. Weitere Kunden sind Familien und/oder Singlehaushalte, die eine Haushaltfshilfe benötigen.</p>
    </div>

    <div class="benefits">
      <h2>Unsere Vorteile</h2>
      <div class="benefit" style="left:43px">
        <svg viewBox="0 0 60 60" style="margin-left:21px"><path d="M4 0h32l14 14v46H4z" fill="var(--red)"/><path d="M36 0v14h14" fill="#fff" opacity=".5"/><rect x="10" y="8" width="12" height="4" fill="#fff"/><rect x="10" y="16" width="12" height="4" fill="#fff"/><text x="27" y="50" font-family="Roboto,Arial,sans-serif" font-size="24" font-weight="700" fill="#fff" text-anchor="middle">$</text></svg>
        <p>Abrechnung mit<br>allen Pflege-<br>kassen möglich</p>
      </div>
      <div class="benefit" style="left:163px">
        <svg viewBox="0 0 60 60" style="margin-left:36px"><path d="M22 0h10v9h9v10h-9v9H22v-9h-9V9h9z" fill="var(--red)"/><path d="M0 44h14l10-4h12c3 0 3 5 0 5H26v2h12l14-8c4-2 7 2 4 5L40 58H0z" fill="var(--red)"/></svg>
        <p>Abrechnung über den<br>Entlastungsbetrag von<br>mind. 125 € mtl. ab<br>Pflegegrad 1 möglich</p>
      </div>
      <div class="benefit" style="left:312px">
        <svg viewBox="0 0 60 60" style="margin-left:21px"><path d="M30 30 16 16c-6-6 0-15 7-12 3 1 5 4 7 6 2-2 4-5 7-6 7-3 13 6 7 12z" fill="var(--red)"/><path d="M0 46h14l10-4h12c3 0 3 5 0 5H26v2h12l14-8c4-2 7 2 4 5L40 60H0z" fill="var(--red)"/></svg>
        <p>Auch über die<br>Verhinderungspflege</p>
      </div>
      <div class="benefit" style="left:460px">
        <svg viewBox="0 0 60 60" style="margin-left:15px"><path d="M0 4h26l12 12v10L22 44v8H0z" fill="var(--red)"/><path d="M26 4v12h12" fill="#fff" opacity=".5"/><path d="M6 42l4-6 3 6 3-4 4 2" stroke="#fff" stroke-width="2" fill="none"/><path d="M50 20l6 6-22 22-8 2 2-8z" fill="var(--red)"/></svg>
        <p>Hilfe bei der<br>Antragsstellung</p>
      </div>
    </div>
  </section>

  <section class="page page--right offers">
    <h2>Die Vielfalt unserer Angebote</h2>
    <p class="body-text">Den Alltag zu bewältigen kann eine echte Herausforderung sein. Egal ob Sie Hilfe beim Einkaufen oder anderen alltäglichen Aktivitäten benötigen, wir helfen gerne.</p>

    <div class="service" style="left:116px;top:195px">
      <div class="tile"><svg viewBox="0 0 72 72"><path d="M12 62V24a16 16 0 0 1 32 0v8"/><path d="M4 64h16v-4H12"/><rect x="38" y="34" width="26" height="30" rx="10"/><circle cx="56" cy="58" r="7"/></svg></div>
      <span>Haushaltshilfe</span>
    </div>
    <div class="service" style="left:329px;top:195px">
      <div class="tile"><svg viewBox="0 0 72 72"><path d="M14 18h40v50H14z"/><path d="M44 18v50l10-2"/><path d="M18 18c0-8 6-12 10-8 2-6 12-6 14 0 4-4 12 0 10 8"/></svg></div>
      <span>Einkaufsservice</span>
    </div>
    <div class="service" style="left:116px;top:386px">
      <div class="tile"><svg viewBox="0 0 72 72"><rect x="12" y="4" width="48" height="64"/><path d="M12 16h48M12 58h48"/><circle cx="36" cy="37" r="14"/><circle cx="36" cy="37" r="9"/><circle cx="38" cy="10" r="2"/><path d="M44 10h10"/></svg></div>
      <span>Wäscheservice</span>
    </div>
    <div class="service" style="left:329px;top:386px">
      <div class="tile"><svg viewBox="0 0 72 72"><path d="M50 4 42 40"/><path d="M36 38l12 4 6 20-26-6z"/><path d="M40 44l-2 14M46 46l2 12"/><circle cx="12" cy="52" r="4"/><circle cx="22" cy="46" r="3"/><circle cx="12" cy="42" r="2"/></svg></div>
      <span>Kehrwoche</span>
    </div>
    <div class="service" style="left:116px;top:578px">
      <div class="tile"><svg viewBox="0 0 72 72"><path d="M34 58 60 30M40 64 66 36M54 28l14 14"/><path d="M14 12l2 5 5 2-5 2-2 5-2-5-5-2 5-2z"/><path d="M30 22l2 6 6 2-6 2-2 6-2-6-6-2 6-2z"/><path d="M40 6l10 10M8 46l12 12"/></svg></div>
      <span>Fensterreinigung</span>
    </div>
    <div class="service" style="left:329px;top:578px">
      <div class="tile"><svg viewBox="0 0 72 72"><path d="M36 66 10 40C2 32 8 16 20 18c8 1 12 8 16 12 4-4 8-11 16-12 12-2 18 14 10 22z"/><path d="M30 50V36a6 6 0 0 1 12 0"/><path d="M36 4v6M20 8l4 5M52 8l-4 5"/></svg></div>
      <span>Alltagsbegleitung</span>
    </div>
  </section>
</div>
</body>
</html>
```